I am looking for help designing my new business cards. I would like rounded edges and a raised logo on the back of the card. I have 2 Logos. One with a boat in it and one without. I'd like the one on the back to be the one that includes the boat and just the name on the front. I have included multiple formats of my logo. Please let me know if you need anymore.

Target Market(s)

Potential buyers and other sales brokers

Industry/Entity Type

Sales - Yacht / Boat Sales

Contact Information for Business Card

Id liike the front to include just the business name portion of the logo along with my name (Colin Wardell), phone number (555.318.2967), website address (www.wardellkeelsales.com) and not my physical address but just "Port Ellis, SC". The back should include my full logo that has the boat included. This portion I'd prefer raised amd take up the majority of the space there. Thanks!!

Colors
0054AA
0677BA
7BADD7
CADEEF
E8F1F8
0094D4
00A9DD
6FCCEA
C7EBF8
E9F6FB

Requirements
Must have
• Double sided
Nice to have
• My email address: Colin@wardellkeelsales.com The NMTG logo somewhere small on the front of the card
Should not have
• My full address, prefer only "Port Ellis, SC"

```html
<!DOCTYPE html>
<html lang="en">
<head>
<meta charset="UTF-8">
<title>Wardell Keel Sales – Business Card</title>
<link href="https://fonts.googleapis.com/css2?family=Montserrat:wght@400;500;700;800&display=swap" rel="stylesheet">
<style>
  :root {
    --navy: #0a3a7a;
    --navy-deep: #072a5c;
    --brand-blue: #0054aa;
    --sky: #0094d4;
    --ink: #333a44;
    --rule: #555a60;
    --paper: #ffffff;
    --backdrop: #3a3a3c;
  }
  * { box-sizing: border-box; margin: 0; padding: 0; }
  html, body { width: 1200px; height: 1200px; overflow: hidden; }
  body {
    background: var(--backdrop);
    font-family: "Montserrat", sans-serif;
    display: flex;
    flex-direction: column;
    align-items: center;
    justify-content: center;
    gap: 60px;
  }
  .card {
    position: relative;
    width: 840px;
    height: 480px;
    border-radius: 36px;
    overflow: hidden;
  }

  /* Front */
  .card-front { background: var(--paper); }
  .wordmark {
    position: absolute;
    left: 0;
    width: 100%;
    text-align: center;
    font-weight: 800;
    line-height: 1;
  }
  .wordmark .name, .wordmark .sub { display: block; }
  .front-wordmark { top: 90px; color: var(--navy); }
  .front-wordmark .name { font-size: 64px; letter-spacing: 2px; padding-left: 2px; }
  .front-wordmark .sub { font-size: 26px; letter-spacing: 8px; padding-left: 8px; margin-top: 10px; }

  .holder {
    position: absolute;
    left: 60px;
    top: 330px;
  }
  .holder-name { color: var(--sky); font-weight: 700; font-size: 30px; letter-spacing: .5px; line-height: 1.2; }
  .holder-company { color: var(--ink); font-weight: 500; font-size: 20px; letter-spacing: .5px; margin-top: 4px; line-height: 1.2; }

  .divider {
    position: absolute;
    left: 440px;
    top: 240px;
    width: 1px;
    height: 150px;
    background: var(--rule);
  }
  .contact-list {
    position: absolute;
    left: 470px;
    top: 235px;
    list-style: none;
  }
  .contact-list li {
    display: flex;
    align-items: center;
    gap: 12px;
    color: var(--ink);
    font-size: 18px;
    line-height: 34px;
    white-space: nowrap;
  }
  .contact-list svg { width: 20px; height: 20px; flex: none; }
  .icon-fill { fill: var(--brand-blue); }
  .icon-line { fill: none; stroke: var(--brand-blue); stroke-width: 2; }

  .band-navy {
    position: absolute; left: 0; bottom: 0;
    width: 500px; height: 24px;
    background: var(--navy);
  }
  .band-sky {
    position: absolute; left: 512px; bottom: 0;
    width: 328px; height: 60px;
    background: var(--sky);
  }

  /* Back */
  .card-back {
    background: radial-gradient(ellipse at 50% 40%, #0d3f82 0%, var(--navy-deep) 80%);
  }
  .boat-art {
    position: absolute;
    left: 220px;
    top: 50px;
    width: 400px;
    height: 210px;
    border-radius: 12px;
    background: linear-gradient(160deg, rgba(255,255,255,.35) 0%, rgba(0,169,221,.55) 60%, rgba(0,148,212,.25) 100%);
  }
  .back-wordmark { top: 290px; color: var(--paper); }
  .back-wordmark .name { font-size: 82px; letter-spacing: 3px; padding-left: 3px; }
  .back-wordmark .sub { font-size: 30px; letter-spacing: 10px; padding-left: 10px; margin-top: 12px; }
</style>
</head>
<body>

<section class="card card-front">
  <div class="wordmark front-wordmark">
    <span class="name">WARDELL</span>
    <span class="sub">KEEL SALES</span>
  </div>

  <div class="holder">
    <p class="holder-name">COLIN WARDELL</p>
    <p class="holder-company">WARDELL KEEL SALES</p>
  </div>

  <div class="divider"></div>

  <ul class="contact-list">
    <li>
      <svg viewBox="0 0 24 24"><path class="icon-fill" d="M6.6 10.8a15 15 0 0 0 6.6 6.6l2.2-2.2a1 1 0 0 1 1-.25 11.4 11.4 0 0 0 3.6.57 1 1 0 0 1 1 1V20a1 1 0 0 1-1 1A17 17 0 0 1 3 4a1 1 0 0 1 1-1h3.5a1 1 0 0 1 1 1c0 1.25.2 2.45.57 3.57a1 1 0 0 1-.25 1z"/></svg>
      (555) 318-2967
    </li>
    <li>
      <svg viewBox="0 0 24 24"><path class="icon-line" d="M3 5h18v14H3z M3 5l9 8 9-8"/></svg>
      colin@wardellkeelsales.com
    </li>
    <li>
      <svg viewBox="0 0 24 24"><circle class="icon-line" cx="12" cy="12" r="9"/><path class="icon-line" d="M3 12h18M12 3c3 3 3 15 0 18M12 3c-3 3-3 15 0 18" stroke-width="1.6"/></svg>
      www.wardellkeelsales.com
    </li>
    <li>
      <svg viewBox="0 0 24 24"><path class="icon-fill" d="M12 2a7 7 0 0 0-7 7c0 5 7 13 7 13s7-8 7-13a7 7 0 0 0-7-7zm0 9.5A2.5 2.5 0 1 1 12 6.5a2.5 2.5 0 0 1 0 5z"/></svg>
      Port Ellis, SC
    </li>
  </ul>

  <div class="band-navy"></div>
  <div class="band-sky"></div>
</section>

<section class="card card-back">
  <div class="boat-art" role="img" aria-label="Illustration of a center-console fishing boat riding over blue waves"></div>
  <div class="wordmark back-wordmark">
    <span class="name">WARDELL</span>
    <span class="sub">KEEL SALES</span>
  </div>
</section>

</body>
</html>
```